Velvet Bloom Marisol's Cleaning Service Business Cards Project

A business card with all contact details with logo design on there (already have a logo) eye catching Logo and contact info on one side, full logo on the back, must target upper class residential and corporate companies, fitness companies, still keep it on the feminine side of things , must look elegant

Target Market(s)

Upper class homes and corporate companies

Industry/Entity Type

Cleaning Service

Contact Information for Business Card

Name: Marisol Denhart
Position: Director
ABN: 47193062857
Email: marisolsvelvetcleaning@brightmail.example
Number: 0418926547

Font styles to use
Decorative

Colors

Designer to choose colors to be used in the design.

Requirements
Must have
• Available Sydney Wide, contact info and logo on one side, full logo on the back
Nice to have
• Professional appearance
Should not have
• Cheap advert looking stuff

```html
<!DOCTYPE html>
<html lang="en">
<head>
<meta charset="utf-8">
<title>Velvet Bloom – Business Card</title>
<link rel="stylesheet" href="https://fonts.googleapis.com/css2?family=Bebas+Neue&family=Cinzel:wght@400;500&family=Josefin+Sans:wght@400&family=Open+Sans:wght@400&display=swap">
<style>
  :root {
    --backdrop: #e8e5e1;
    --card-dark: #2d3240;
    --card-light: #ffffff;
    --silver: #b9bcc2;
    --silver-soft: #9ea2aa;
    --emblem-top: rgba(185, 188, 194, 0.22);
    --emblem-bottom: rgba(185, 188, 194, 0.08);
    --ink: #1f2230;
    --ink-body: #1c1c1c;
  }
  * { margin: 0; padding: 0; box-sizing: border-box; }
  html, body {
    width: 1200px;
    height: 1000px;
    overflow: hidden;
    background: var(--backdrop);
  }
  .canvas {
    position: relative;
    width: 1200px;
    height: 1000px;
  }
  .card {
    position: absolute;
    left: 266px;
    width: 666px;
    border-radius: 22px;
    box-shadow: 0 4px 14px rgba(0, 0, 0, 0.18);
  }
  .card--front {
    top: 75px;
    height: 396px;
    background: var(--card-dark);
  }
  .card--back {
    top: 533px;
    height: 397px;
    background: var(--card-light);
  }

  /* Front: emblem and ornament area */
  .emblem {
    position: absolute;
    left: 164px;
    top: 64px;
    width: 340px;
    height: 192px;
    border-radius: 10px;
    background: linear-gradient(180deg, var(--emblem-top), var(--emblem-bottom));
  }

  /* Front: brand name */
  .brand {
    position: absolute;
    left: 0;
    right: 0;
    top: 270px;
    text-align: center;
  }
  .brand__name {
    font-family: "Cinzel", serif;
    font-weight: 500;
    font-size: 38px;
    letter-spacing: 1px;
    color: var(--silver);
    line-height: 1;
  }
  .brand__tagline {
    margin-top: 12px;
    font-family: "Josefin Sans", sans-serif;
    font-size: 13.5px;
    letter-spacing: 3.8px;
    color: var(--silver-soft);
    text-transform: uppercase;
  }

  /* Back: contact block */
  .person {
    position: absolute;
    right: calc(666px - 251px);
    top: 170px;
    text-align: right;
  }
  .person__name {
    font-family: "Bebas Neue", sans-serif;
    font-size: 29px;
    color: var(--ink);
    line-height: 1;
    letter-spacing: 0.3px;
  }
  .person__role {
    margin-top: 6px;
    font-family: "Open Sans", sans-serif;
    font-size: 15px;
    color: var(--ink-body);
  }
  .divider {
    position: absolute;
    left: 270px;
    top: 170px;
    width: 1.5px;
    height: 55px;
    background: var(--ink);
  }
  .contact {
    position: absolute;
    left: 286px;
    top: 166px;
    list-style: none;
    font-family: "Open Sans", sans-serif;
    font-size: 16px;
    color: var(--ink-body);
    line-height: 21.5px;
  }
  .contact__item {
    display: flex;
    align-items: center;
    gap: 6px;
  }
  .contact__icon {
    width: 14px;
    height: 14px;
    flex: none;
  }
</style>
</head>
<body>
<main class="canvas">
  <section class="card card--front" aria-label="Card front">
    <div class="emblem" role="img" aria-label="Brand emblem with a decorative silver flourish beneath it"></div>
    <div class="brand">
      <p class="brand__name">VELVET BLOOM</p>
      <p class="brand__tagline">Marisol's Cleaning Service</p>
    </div>
  </section>

  <section class="card card--back" aria-label="Card back">
    <div class="person">
      <p class="person__name">MARISOL DENHART</p>
      <p class="person__role">Director</p>
    </div>
    <div class="divider"></div>
    <ul class="contact">
      <li class="contact__item">ABN: 47193062857</li>
      <li class="contact__item">
        <svg class="contact__icon" viewBox="0 0 24 24" fill="none" stroke="#1c1c1c" stroke-width="2" stroke-linejoin="round" aria-hidden="true">
          <path d="M5 3h4l2 5-2.5 1.5a11 11 0 0 0 6 6L16 13l5 2v4a2 2 0 0 1-2 2A16 16 0 0 1 3 5a2 2 0 0 1 2-2z"/>
        </svg>
        0418926547
      </li>
      <li class="contact__item">
        <svg class="contact__icon" viewBox="0 0 24 24" fill="none" stroke="#1c1c1c" stroke-width="2" stroke-linejoin="round" aria-hidden="true">
          <rect x="3" y="5" width="18" height="14" rx="1"/>
          <path d="M3 6l9 7 9-7"/>
        </svg>
        marisolsvelvetcleaning@brightmail.example
      </li>
    </ul>
  </section>
</main>
</body>
</html>
```